New Business Card Design Project

We require a business card design for Zelvaquin, a newly established Indian company.
Our focus is on the development, manufacturing, and export of a diverse array of pharmaceutical products on a global scale. The card should convey a professional appearance, as our primary markets are in Africa, China, and Southeast Asian nations.
We envision a two-sided business card, with the reverse side dedicated to a logo set against a solid color or an elegantly designed pattern. The corners should be rounded. We would appreciate seeing both horizontal and vertical design options. We trust the designer to utilize their expertise in creating this design.

The content for the business card is included in the attached Word file.

Target Market(s)

Our primary markets are in Africa, China, and Southeast Asian, Latin America, Maldives, Sri Lanka

Industry/Entity Type

Pharmaceutical Manufacturing and Export

Contact Information for Business Card

Colors

Designer to choose colors to be used in the design.

Requirements
Must have
• The reverse side of the business card features solely the logo along with the tagline, "Remedies of Life."
Should not have
• The logo should not exceed two instances, encompassing both the front and back sides of the card.

```html
<!DOCTYPE html>
<html lang="en">
<head>
<meta charset="UTF-8">
<title>Zelvaquin Business Card</title>
<link href="https://fonts.googleapis.com/css2?family=Poppins:wght@400;500;600;700&display=swap" rel="stylesheet">
<style>
  :root {
    --page-bg: #2a2b2d;
    --card-white: #f7f7f7;
    --brand-blue: #259fd9;
    --brand-blue-deep: #1d86b9;
    --brand-red: #e85c45;
    --ink: #2b2b2b;
    --ink-soft: #3d3d3d;
    --navy: #155b80;
    --bubble-blue: rgba(37, 159, 217, 0.14);
    --bubble-red: rgba(232, 92, 69, 0.13);
    --bubble-white: rgba(255, 255, 255, 0.14);
  }
  * { margin: 0; padding: 0; box-sizing: border-box; }
  html, body { width: 1200px; height: 900px; overflow: hidden; }
  body {
    background: var(--page-bg);
    font-family: "Poppins", sans-serif;
    position: relative;
  }
  .card {
    position: absolute;
    top: 110px;
    width: 400px;
    height: 680px;
    border-radius: 44px;
    overflow: hidden;
  }
  .card-front { left: 150px; background: var(--card-white); }
  .card-back { left: 650px; background: var(--brand-blue); }
  .card-art { position: absolute; inset: 0; width: 100%; height: 100%; }
  .card-content {
    position: relative;
    z-index: 1;
    display: flex;
    flex-direction: column;
    align-items: center;
    text-align: center;
  }
  .brand-lockup {
    display: flex;
    align-items: center;
    gap: 12px;
  }
  .brand-dot {
    width: 26px; height: 26px; border-radius: 50%;
  }
  .brand-name {
    font-weight: 700;
    font-size: 50px;
    letter-spacing: -0.5px;
    line-height: 1;
  }
  .card-front .card-content { padding-top: 120px; }
  .card-front .brand-dot { background: var(--brand-red); }
  .card-front .brand-name { color: var(--brand-blue); }
  .person-name {
    margin-top: 34px;
    color: var(--brand-red);
    font-weight: 700;
    font-size: 19px;
    letter-spacing: 0.3px;
  }
  .person-role {
    color: var(--ink-soft);
    font-size: 17px;
    margin-top: 2px;
  }
  .contact-list {
    list-style: none;
    margin-top: 30px;
    font-size: 16.5px;
    color: var(--ink);
    line-height: 1.65;
  }
  .contact-list li { display: flex; align-items: center; justify-content: center; gap: 8px; }
  .contact-icon { width: 16px; height: 16px; flex: none; }
  .address {
    margin-top: 28px;
    font-size: 17px;
    color: var(--ink);
    line-height: 1.5;
  }
  .tagline {
    font-weight: 700;
    letter-spacing: 0.6px;
    text-transform: uppercase;
  }
  .card-front .tagline {
    margin-top: 40px;
    font-size: 15px;
    color: #1a1a1a;
  }
  .card-back .card-content { padding-top: 230px; }
  .card-back .brand-dot { background: #ffffff; }
  .card-back .brand-name { color: #ffffff; }
  .card-back .tagline {
    margin-top: 14px;
    font-size: 16px;
    color: var(--navy);
  }
</style>
</head>
<body>

  <section class="card card-front" aria-label="Front of business card">
    <svg class="card-art" viewBox="0 0 400 680" aria-hidden="true">
      <circle cx="120" cy="330" r="28" fill="var(--bubble-blue)"/>
      <circle cx="272" cy="340" r="38" fill="var(--bubble-red)"/>
      <circle cx="100" cy="480" r="32" fill="var(--bubble-red)"/>
      <circle cx="305" cy="445" r="16" fill="var(--bubble-blue)"/>
      <circle cx="215" cy="560" r="40" fill="var(--bubble-blue)"/>
      <circle cx="290" cy="625" r="20" fill="var(--bubble-red)"/>
      <path d="M0 540 Q 60 505 120 540 L 245 680 L 0 680 Z" fill="var(--brand-blue)"/>
      <path d="M310 680 L 310 520 Q 310 455 360 452 Q 400 452 400 490 L 400 680 Z" fill="var(--brand-red)"/>
    </svg>
    <div class="card-content">
      <div class="brand-lockup">
        <span class="brand-dot"></span>
        <span class="brand-name">Zelvaquin</span>
      </div>
      <p class="person-name">ROHAN K. TAVARE</p>
      <p class="person-role">CEO Of Zelvaquin</p>
      <ul class="contact-list">
        <li>
          <svg class="contact-icon" viewBox="0 0 16 16" aria-hidden="true"><rect x="4" y="1" width="8" height="14" rx="1.5" fill="none" stroke="var(--brand-blue)" stroke-width="1.4"/><line x1="7" y1="12.5" x2="9" y2="12.5" stroke="var(--brand-blue)" stroke-width="1.4"/></svg>
          +919812345670
        </li>
        <li>
          <svg class="contact-icon" viewBox="0 0 16 16" aria-hidden="true"><rect x="1" y="3.5" width="14" height="9" fill="var(--brand-blue)"/><path d="M1 3.5 L8 9 L15 3.5" fill="none" stroke="#fff" stroke-width="1.2"/></svg>
          rtavare@zelvaquin.com
        </li>
        <li>
          <svg class="contact-icon" viewBox="0 0 16 16" aria-hidden="true"><g fill="none" stroke="var(--brand-blue)" stroke-width="1.2"><circle cx="8" cy="8" r="6.5"/><ellipse cx="8" cy="8" rx="3" ry="6.5"/><line x1="1.5" y1="8" x2="14.5" y2="8"/></g></svg>
          www.zelvaquin.com
        </li>
      </ul>
      <p class="address">12, Suryoday Colony<br>Nandgaon, 411020, India</p>
      <p class="tagline">Remedies of Life</p>
    </div>
  </section>

  <section class="card card-back" aria-label="Back of business card">
    <svg class="card-art" viewBox="0 0 400 680" aria-hidden="true">
      <circle cx="110" cy="410" r="30" fill="var(--bubble-white)"/>
      <circle cx="250" cy="420" r="42" fill="var(--bubble-white)"/>
      <circle cx="150" cy="500" r="36" fill="var(--bubble-white)"/>
      <circle cx="245" cy="490" r="22" fill="var(--bubble-white)"/>
      <circle cx="320" cy="480" r="16" fill="var(--bubble-white)"/>
      <circle cx="220" cy="565" r="44" fill="var(--bubble-white)"/>
      <circle cx="340" cy="620" r="22" fill="var(--bubble-white)"/>
      <path d="M0 590 Q 50 560 110 585 L 250 680 L 0 680 Z" fill="var(--brand-blue-deep)"/>
      <path d="M330 680 L 330 510 Q 330 450 370 448 Q 400 448 400 470 L 400 680 Z" fill="var(--brand-blue-deep)"/>
    </svg>
    <div class="card-content">
      <div class="brand-lockup">
        <span class="brand-dot"></span>
        <span class="brand-name">Zelvaquin</span>
      </div>
      <p class="tagline">Remedies of Life</p>
    </div>
  </section>

</body>
</html>
```